Newsletter (nur grafisch) Kreditvermittlung Lumo-Finanz
Aufgabenstellung
Kreditsuchende stellen bei uns EINEN Kreditantrag und wir verhandeln mit bis zu 20 Banken und präsentieren dem Kunden dann das beste Angebot absolut kostenlos und unverbindlich.
Spezielle Landingpage:
www.lumo-finanz.de/kredit.htm
Wir wollen eine Newslettervorlage, die dieses Angebot bewirbt. Wir brauchen nur das Design - die Umsetzung in html können wir dann selbst.
Die notwendigen Bilddateien müssen vom Gewinner zur Verfügung gestellt werden.
Skizzenhafte Ausführung bei Dingen, die klar sind (z.B. Header) genügen.
Text kann Fülltext verwendet werden oder Sie schreiben schnell eine Kleinigkeit, inspiriert durch die Landingpage.
Wir sind mittlerweile betriebsblind und für jeden frischen Wind dankbar!
Langfristige Zusammenarbeit:
Wir benötigen ständig Grafiken, Werbemittel und html-Arbeiten. Der Gewinner dieses Wettbewerbs kann sich auf weitere lukrative Aufträge freuen!

```html
<!DOCTYPE html>
<html lang="de">
<head>
<meta charset="utf-8">
<title>Lumo-Finanz Newsletter</title>
<link rel="stylesheet" href="https://fonts.googleapis.com/css2?family=Arimo:wght@400;700&display=swap">
<style>
  :root {
    --teal-dark: #0b4552;
    --teal-mid: #457a84;
    --teal-light: #b9d6da;
    --sand: #d6cfc2;
    --ink: #111;
    --page-top: #f2f0ed;
    --page-bottom: #e4e1dc;
    --band: #dcd9d3;
    --muted: #8a8a8a;
    --green: #6cb23c;
    --green-dark: #3f8a1f;
  }
  * { margin: 0; padding: 0; box-sizing: border-box; }
  html, body { width: 1200px; height: 1036px; overflow: hidden; }
  body {
    position: relative;
    font-family: "Arimo", Arial, sans-serif;
    color: var(--ink);
    background: linear-gradient(to bottom, var(--page-top) 0, #ebe9e5 323px, var(--band) 324px, #e0ddd8 600px, var(--page-bottom) 1036px);
  }
  .newsletter {
    position: absolute; left: 149px; top: 19px; width: 903px; height: 945px;
    background: #fff;
    box-shadow: 0 0 8px rgba(0,0,0,.12);
  }
  .header { position: absolute; left: 0; top: 0; width: 903px; height: 134px; }
  .header__fade {
    position: absolute; left: 230px; top: 66px; width: 502px; height: 32px;
    background: linear-gradient(to right, #fff 0, var(--teal-light) 55%, var(--teal-light) 100%);
  }
  .header__sand { position: absolute; left: 583px; top: 66px; width: 62px; height: 32px; background: var(--sand); }
  .header__teal { position: absolute; left: 646px; top: 66px; width: 257px; height: 32px; background: var(--teal-mid); }
  .header__band { position: absolute; left: 0; top: 101px; width: 903px; height: 31px; background: var(--teal-dark); }
  .brand {
    position: absolute; left: 26px; top: 40px;
    font-size: 66px; font-weight: 700; color: var(--teal-dark); line-height: 1;
    letter-spacing: 2px;
  }
  .tagline {
    position: absolute; left: 276px; top: 108px;
    font-size: 16px; font-weight: 700; color: #fff; letter-spacing: .8px;
  }
  .headline {
    position: absolute; left: 37px; top: 162px;
    font-size: 21px; font-weight: 700; color: var(--teal-dark);
  }
  .hero-photo {
    position: absolute; left: 45px; top: 226px; width: 350px; height: 270px;
    background: radial-gradient(ellipse at 50% 55%, #5a5d66 0, #8a8c93 40%, #f3f3f3 75%, #fff 100%);
  }
  .benefits { position: absolute; left: 443px; top: 280px; list-style: none; }
  .benefits li { position: relative; height: 49px; padding-left: 62px; font-size: 19px; line-height: 44px; }
  .benefits svg { position: absolute; left: 0; top: 3px; }
  .section { position: absolute; left: 37px; width: 760px; font-size: 17.5px; line-height: 28px; }
  .section h2 { font-size: 17.5px; font-weight: 700; color: var(--teal-dark); line-height: 28px; }
  .section strong { font-weight: 700; }
  .section--time { top: 511px; }
  .section--free { top: 617px; }
  .section--trust { top: 727px; }
  .seal {
    position: absolute; left: 703px; top: 526px; width: 140px; height: 163px;
    border: 1px solid #cfd6d8; background: linear-gradient(to bottom, #fff 0, #f2f5f6 55%, #8fb3b9 75%, #4c7f88 100%);
    box-shadow: 0 1px 4px rgba(0,0,0,.2);
  }
  .cta {
    position: absolute; left: 198px; top: 852px; width: 494px; height: 48px;
    background: linear-gradient(to bottom, #5a9aa4, #3d7d88);
    border: 1px solid #2f6570;
    color: #fff; font-size: 20.5px; font-weight: 700; text-align: center; line-height: 46px;
    text-shadow: 0 1px 1px rgba(0,0,0,.3);
  }
  .footer { position: absolute; top: 985px; font-size: 12px; color: var(--muted); }
  .footer--left { left: 173px; }
  .footer--right { left: 902px; }
</style>
</head>
<body>
  <main class="newsletter">
    <header class="header">
      <div class="header__fade"></div>
      <div class="header__sand"></div>
      <div class="header__teal"></div>
      <div class="header__band"></div>
      <div class="brand">LUMO</div>
      <div class="tagline">KREDIT - seit 35 Jahren</div>
    </header>

    <h1 class="headline">Der beste Kredit - kostenlos, schnell und fair</h1>

    <div class="hero-photo" role="img" aria-label="Foto: Beraterin und Berater im Anzug, die einladend zur Seite zeigen"></div>

    <ul class="benefits">
      <li><svg width="38" height="38" viewBox="0 0 38 38"><circle cx="19" cy="19" r="18" fill="var(--green)" stroke="var(--green-dark)" stroke-width="1.5"/><circle cx="19" cy="19" r="11" fill="#fff" opacity=".25"/><path d="M11 19l6 6 10-12" fill="none" stroke="#fff" stroke-width="3.5" stroke-linecap="round" stroke-linejoin="round"/></svg>Das beste Kreditangebot von 20 Banken</li>
      <li><svg width="38" height="38" viewBox="0 0 38 38"><circle cx="19" cy="19" r="18" fill="var(--green)" stroke="var(--green-dark)" stroke-width="1.5"/><circle cx="19" cy="19" r="11" fill="#fff" opacity=".25"/><path d="M11 19l6 6 10-12" fill="none" stroke="#fff" stroke-width="3.5" stroke-linecap="round" stroke-linejoin="round"/></svg>kostenlos und unverbindlich</li>
      <li><svg width="38" height="38" viewBox="0 0 38 38"><circle cx="19" cy="19" r="18" fill="var(--green)" stroke="var(--green-dark)" stroke-width="1.5"/><circle cx="19" cy="19" r="11" fill="#fff" opacity=".25"/><path d="M11 19l6 6 10-12" fill="none" stroke="#fff" stroke-width="3.5" stroke-linecap="round" stroke-linejoin="round"/></svg>schnelle Bearbeitung</li>
      <li><svg width="38" height="38" viewBox="0 0 38 38"><circle cx="19" cy="19" r="18" fill="var(--green)" stroke="var(--green-dark)" stroke-width="1.5"/><circle cx="19" cy="19" r="11" fill="#fff" opacity=".25"/><path d="M11 19l6 6 10-12" fill="none" stroke="#fff" stroke-width="3.5" stroke-linecap="round" stroke-linejoin="round"/></svg>auch Kredite ohne Krevis</li>
    </ul>

    <section class="section section--time">
      <h2>Sparen Sie Zeit und Geld!</h2>
      <p>Ein Antrag genügt. Wir verhandeln für Sie mit 20 Banken und präsentieren<br>Ihnen das beste Kreditangebot. Bequemer geht es nicht.</p>
    </section>

    <section class="section section--free">
      <h2>Garantiert kostenlos und unverbindlich</h2>
      <p>Sie bezahlen für unseren Service keinen Cent. Auch wenn Ihre Kreditanfrage<br>abgelehnt werden sollte oder Sie es nicht annehmen möchten.</p>
    </section>

    <div class="seal" role="img" aria-label="Qualitätssiegel"></div>

    <section class="section section--trust">
      <h2>Sicherheit durch Erfahrung</h2>
      <p>Lumo-Finanz hilft auch dann noch, wenn andere bereits abgelehnt haben. Tausende zufriedene<br>Kunden bestätigen das. <strong>Profitieren auch Sie von unserer langjährigen Erfahrung.</strong></p>
    </section>

    <div class="cta">Jetzt unverbindliches Kreditangebot anfordern!</div>
  </main>

  <div class="footer footer--left">Wird dieser Newsletter falsch angezeigt? Hier melden</div>
  <div class="footer footer--right">www.lumo-finanz.de</div>
</body>
</html>
```